Info Graphic for our IT Staff Augmentation Page

Our offering would be:
-Programmers
-Project Managers
-Testers
-Solutions Architects
-Designers
-Applications Adminstrators
-Network Administrators
-PC/Help Desk Support

We would offer: Onsite | Offsite | Remote

Please see our Website for Content Ideas:
http://staging.brovelanetech.example/staff-augmentation/

**** The background video will not stay there in the header. We would be looking to replace with your info graphic. Dimensions should be at least 2000 x 400

Industry/Entity Type

It Support

Requirements
Should not have
• The example info graphic uploaded here is to show the scope of the project. Do not try to simply duplicate...will be rejected and you will waist your time and mine. Please create an interpretation with the service offerings included and look at the existing content in the staff augmentation page to get ideas.

```html
<!DOCTYPE html>
<html lang="en">
<head>
<meta charset="utf-8">
<title>Staff Augmentation Header Banners</title>
<link rel="stylesheet" href="https://fonts.googleapis.com/css2?family=Fredoka:wght@600&family=Source+Sans+3:wght@400&family=Handlee&display=swap">
<style>
  :root {
    --page: #ffffff;
    --ink-light: #ffffff;
    --ink-dark: #333333;
    --charcoal: #333333;
    --lime: #e0e43a;
    --ring-grey: #7a7a7a;
    --line-grey: #8a8a8a;
    --night-deep: #07111d;
    --night-mid: #1f3d5c;
    --sky-light: #a9c3d6;
    --sky-mid: #4d6f8e;
    --sun-core: #fff23d;
    --sun-glow: #fffbd6;
  }
  html, body {
    margin: 0;
    padding: 0;
    width: 1200px;
    height: 1000px;
    overflow: hidden;
    background: var(--page);
  }
  .sheet {
    position: relative;
    width: 1200px;
    height: 1000px;
  }
  .banner {
    position: absolute;
    left: 90px;
    width: 1022px;
    height: 204px;
    display: block;
  }
  .banner--night { top: 89px; }
  .banner--sun { top: 380px; }
  .banner--lime { top: 689px; }

  .headline {
    font-family: "Fredoka", "Arial Rounded MT Bold", sans-serif;
    font-weight: 600;
    font-size: 25px;
    letter-spacing: 0.5px;
  }
  .tagline {
    font-family: "Source Sans 3", "Myriad Pro", sans-serif;
    font-size: 15.5px;
  }
  .offer-lead {
    font-family: "Handlee", cursive;
    font-size: 17px;
  }
  .role {
    font-family: "Source Sans 3", "Myriad Pro", sans-serif;
    font-size: 14px;
  }
  .mode-label {
    font-family: "Source Sans 3", "Myriad Pro", sans-serif;
    font-size: 12px;
  }
  .link-line {
    stroke-width: 1.2;
    stroke-dasharray: 3 3;
    fill: none;
  }
</style>
</head>
<body>
<main class="sheet">

  <!-- Blue night variant -->
  <svg class="banner banner--night" viewBox="0 0 1022 204" xmlns="http://www.w3.org/2000/svg">
    <defs>
      <linearGradient id="nightBackdrop" x1="0" y1="0" x2="1" y2="1">
        <stop offset="0" stop-color="var(--night-mid)"/>
        <stop offset="0.5" stop-color="#2e4f70"/>
        <stop offset="1" stop-color="var(--night-deep)"/>
      </linearGradient>
      <radialGradient id="nightStage" cx="0.45" cy="0.3" r="0.8">
        <stop offset="0" stop-color="var(--sky-light)"/>
        <stop offset="1" stop-color="var(--sky-mid)"/>
      </radialGradient>
    </defs>
    <rect width="1022" height="204" fill="url(#nightBackdrop)" role="img" aria-label="Blurred photo of a modern glass office building in dark blue tones"/>
    <path d="M165,0 A350.3,350.3 0 0 0 275,204 L740,204 A350.3,350.3 0 0 0 850,0 Z" fill="url(#nightStage)" role="img" aria-label="Lighter blurred view of the same office building"/>
    <path d="M165,0 A350.3,350.3 0 0 0 275,204 M740,204 A350.3,350.3 0 0 0 850,0" fill="none" stroke="var(--ink-light)" stroke-width="5"/>

    <g fill="var(--ink-light)">
      <text class="headline" x="511" y="43" text-anchor="middle" textLength="588" lengthAdjust="spacingAndGlyphs">CUSTOM SOFTWARE DEISGN FOR YOUR BUSINESS</text>
      <text class="tagline" x="511" y="65" text-anchor="middle" textLength="358" lengthAdjust="spacingAndGlyphs">CALL TODAY FOR A FREE BRAINSTORMING SESSION!</text>
      <text class="offer-lead" x="511" y="103" text-anchor="middle" fill-opacity="0.85">We would offer</text>
    </g>

    <g class="roles roles--left" fill="var(--ink-light)" text-anchor="end">
      <text class="role" x="155" y="75">Testers</text>
      <text class="role" x="158" y="96">Programmers</text>
      <text class="role" x="167" y="117">Project Managers</text>
      <text class="role" x="179" y="138">Solutions Architects</text>
    </g>
    <g class="roles roles--right" fill="var(--ink-light)">
      <text class="role" x="864" y="75">Designers</text>
      <text class="role" x="858" y="96">PC/Help Desk Support</text>
      <text class="role" x="848" y="117">Network Administrators</text>
      <text class="role" x="837" y="138">Applications Adminstrators</text>
    </g>

    <g class="delivery-modes">
      <g stroke="var(--ink-light)" class="link-line">
        <line x1="400" y1="157" x2="345" y2="204"/>
        <line x1="441" y1="150" x2="486" y2="164"/>
        <line x1="536" y1="164" x2="580" y2="150"/>
        <line x1="622" y1="157" x2="675" y2="204"/>
      </g>
      <g fill="none" stroke="var(--ink-light)" stroke-width="4">
        <circle cx="417" cy="139" r="25"/>
        <circle cx="511" cy="171" r="25"/>
        <circle cx="604" cy="139" r="25"/>
      </g>
      <g fill="var(--ink-light)" text-anchor="middle">
        <text class="mode-label" x="417" y="143">Onsite</text>
        <text class="mode-label" x="511" y="175">Offsite</text>
        <text class="mode-label" x="604" y="143">Remote</text>
      </g>
    </g>
  </svg>

  <!-- Yellow sun variant -->
  <svg class="banner banner--sun" viewBox="0 0 1022 204" xmlns="http://www.w3.org/2000/svg">
    <defs>
      <radialGradient id="sunStage" cx="0.25" cy="0.65" r="0.9">
        <stop offset="0" stop-color="var(--sun-core)"/>
        <stop offset="0.55" stop-color="#fff89a"/>
        <stop offset="1" stop-color="var(--sun-glow)"/>
      </radialGradient>
    </defs>
    <rect width="1022" height="204" fill="var(--charcoal)"/>
    <path d="M165,0 A350.3,350.3 0 0 0 275,204 L740,204 A350.3,350.3 0 0 0 850,0 Z" fill="url(#sunStage)" role="img" aria-label="Bright yellow light rays glowing behind the headline"/>
    <path d="M165,0 A350.3,350.3 0 0 0 275,204 M740,204 A350.3,350.3 0 0 0 850,0" fill="none" stroke="var(--ink-light)" stroke-width="5"/>

    <g fill="var(--ink-dark)">
      <text class="headline" x="511" y="43" text-anchor="middle" textLength="588" lengthAdjust="spacingAndGlyphs">CUSTOM SOFTWARE DEISGN FOR YOUR BUSINESS</text>
      <text class="tagline" x="511" y="65" text-anchor="middle" textLength="358" lengthAdjust="spacingAndGlyphs">CALL TODAY FOR A FREE BRAINSTORMING SESSION!</text>
      <text class="offer-lead" x="511" y="103" text-anchor="middle">We would offer</text>
    </g>

    <g class="roles roles--left" fill="var(--ink-light)" text-anchor="end">
      <text class="role" x="155" y="75">Testers</text>
      <text class="role" x="158" y="96">Programmers</text>
      <text class="role" x="167" y="117">Project Managers</text>
      <text class="role" x="179" y="138">Solutions Architects</text>
    </g>
    <g class="roles roles--right" fill="var(--ink-light)">
      <text class="role" x="864" y="75">Designers</text>
      <text class="role" x="858" y="96">PC/Help Desk Support</text>
      <text class="role" x="848" y="117">Network Administrators</text>
      <text class="role" x="837" y="138">Applications Adminstrators</text>
    </g>

    <g class="delivery-modes">
      <g stroke="var(--ink-dark)" class="link-line">
        <line x1="400" y1="157" x2="345" y2="204"/>
        <line x1="441" y1="150" x2="486" y2="164"/>
        <line x1="536" y1="164" x2="580" y2="150"/>
        <line x1="622" y1="157" x2="675" y2="204"/>
      </g>
      <g fill="none" stroke="var(--ink-dark)" stroke-width="4.5">
        <circle cx="417" cy="139" r="25"/>
        <circle cx="511" cy="171" r="25"/>
        <circle cx="604" cy="139" r="25"/>
      </g>
      <g fill="var(--ink-dark)" text-anchor="middle">
        <text class="mode-label" x="417" y="143">Onsite</text>
        <text class="mode-label" x="511" y="175">Offsite</text>
        <text class="mode-label" x="604" y="143">Remote</text>
      </g>
    </g>
  </svg>

  <!-- Lime and charcoal variant -->
  <svg class="banner banner--lime" viewBox="0 0 1022 204" xmlns="http://www.w3.org/2000/svg">
    <rect width="1022" height="204" fill="var(--lime)"/>
    <polygon points="156,0 865,0 748,204 273,204" fill="var(--charcoal)"/>

    <g fill="var(--lime)">
      <text class="headline" x="511" y="52" text-anchor="middle" textLength="588" lengthAdjust="spacingAndGlyphs">CUSTOM SOFTWARE DEISGN FOR YOUR BUSINESS</text>
      <text class="tagline" x="511" y="73" text-anchor="middle" textLength="358" lengthAdjust="spacingAndGlyphs">CALL TODAY FOR A FREE BRAINSTORMING SESSION!</text>
      <text class="offer-lead" x="511" y="111" text-anchor="middle">We would offer</text>
    </g>

    <g class="roles roles--left" fill="var(--ink-dark)" text-anchor="end">
      <text class="role" x="175" y="71">Testers</text>
      <text class="role" x="186" y="96">Programmers</text>
      <text class="role" x="198" y="121">Project Managers</text>
      <text class="role" x="213" y="146">Solutions Architects</text>
    </g>
    <g class="roles roles--right" fill="var(--ink-dark)">
      <text class="role" x="850" y="71">Designers</text>
      <text class="role" x="835" y="96">PC/Help Desk Support</text>
      <text class="role" x="823" y="121">Network Administrators</text>
      <text class="role" x="808" y="146">Applications Adminstrators</text>
    </g>

    <g class="delivery-modes">
      <g stroke="var(--line-grey)" class="link-line">
        <line x1="400" y1="157" x2="345" y2="204"/>
        <line x1="441" y1="150" x2="486" y2="164"/>
        <line x1="536" y1="164" x2="580" y2="150"/>
        <line x1="622" y1="157" x2="675" y2="204"/>
      </g>
      <g fill="none" stroke="var(--ring-grey)" stroke-width="4.5">
        <circle cx="417" cy="139" r="25"/>
        <circle cx="511" cy="171" r="25"/>
        <circle cx="604" cy="139" r="25"/>
      </g>
      <g fill="var(--lime)" text-anchor="middle">
        <text class="mode-label" x="417" y="143">Onsite</text>
        <text class="mode-label" x="511" y="175">Offsite</text>
        <text class="mode-label" x="604" y="143">Remote</text>
      </g>
    </g>
  </svg>

</main>
</body>
</html>
```